Business card design for a engineering company

I need a double sided business card design for my company "Velbrook Stream Systems". The card will be used in Malaysia. Sleek and professional, with a little design flare to it.
Information to showcase:
1. Company logo
2. Name, title, phone, email address, website address
3. our products "Pumping technology, Valve & actuation, Air Moving Technology
Example:
Mark Dovan
Business manager
mark.dovan@velbrook-example.com
www.velbrook-example.com.my
- Pumping technology
- Valve & actuation
- Air moving technology
Target Market(s)
engineers, purchasing managers
Industry/Entity Type
Business
Contact Information for Business Card
Mark Dovan
Business manager
mark.dovan@velbrook-example.com
www.velbrook-example.com.my
- Pumping technology
- Valve & actuation
- Air moving technology
catch phrase : "Solving flow challenges, exceeding expectations"

```html
<!DOCTYPE html>
<html lang="en">
<head>
<meta charset="utf-8">
<title>Velbrook Stream Systems – Business Card</title>
<link rel="stylesheet" href="https://fonts.googleapis.com/css2?family=Source+Sans+3:wght@400;600;700&display=swap">
<style>
  :root {
    --backdrop: #3b3b3d;
    --card: #1b1b1d;
    --card-edge: #2a2a2d;
    --orange: #f39a1e;
    --slate: #2f4a58;
    --text-light: #d9d9d9;
    --divider: #2c2c30;
  }
  * { box-sizing: border-box; margin: 0; padding: 0; }
  html, body {
    width: 1200px; height: 900px; overflow: hidden;
    background: var(--backdrop);
    font-family: "Source Sans 3", "Helvetica Neue", Arial, sans-serif;
  }
  .card-set {
    position: absolute; inset: 0;
    display: flex; align-items: center; justify-content: center; gap: 40px;
  }
  .card {
    width: 540px; height: 310px;
    background: var(--card);
    border: 1px solid var(--card-edge);
    border-radius: 20px;
    position: relative;
    box-shadow: 0 14px 30px rgba(0,0,0,.35);
  }
  /* Front */
  .card-front { display: flex; }
  .brand-panel {
    width: 250px; height: 100%;
    border-right: 1px solid var(--divider);
    display: flex; align-items: center; justify-content: center; gap: 14px;
  }
  .brand-dot {
    width: 26px; height: 26px; border-radius: 50%;
    background: var(--orange); flex: none;
  }
  .brand-panel .brand-name {
    color: var(--orange); font-weight: 700; font-size: 28px; line-height: 1.05;
  }
  .contact-panel { padding: 52px 0 0 32px; flex: 1; }
  .person-name {
    color: var(--orange); font-weight: 700; font-size: 19px; letter-spacing: .02em;
  }
  .person-title { color: var(--text-light); font-size: 15px; margin-top: 2px; }
  .contact-list { list-style: none; margin-top: 22px; }
  .contact-list li {
    color: var(--text-light); font-size: 14px; line-height: 22px;
    display: flex; align-items: center; gap: 8px; white-space: nowrap;
  }
  .contact-list svg { width: 11px; height: 11px; fill: var(--orange); flex: none; }
  .tagline {
    color: var(--orange); font-size: 21px; line-height: 1.2; margin-top: 22px;
  }
  /* Back */
  .card-back {
    display: flex; flex-direction: column; align-items: center; justify-content: center;
  }
  .back-brand { display: flex; align-items: center; gap: 14px; }
  .back-brand .brand-square {
    width: 36px; height: 36px; background: var(--orange); flex: none;
  }
  .back-brand .brand-name {
    color: var(--slate); font-weight: 700; font-size: 34px; letter-spacing: .02em;
  }
  .product-lines {
    margin-top: 48px; text-align: center;
    color: var(--orange); font-size: 15px; line-height: 22px;
  }
  .product-lines .sep { margin: 0 12px; }
</style>
</head>
<body>
<main class="card-set">
  <section class="card card-front" aria-label="Business card front">
    <div class="brand-panel">
      <span class="brand-dot"></span>
      <span class="brand-name">Velbrook<br>Stream<br>Systems</span>
    </div>
    <div class="contact-panel">
      <p class="person-name">MARK DOVAN</p>
      <p class="person-title">Business manager</p>
      <ul class="contact-list">
        <li><svg viewBox="0 0 12 12"><path d="M1 3c0-1 1-2 2-2h1l1 3-1.5 1c.6 1.4 1.6 2.4 3 3L7.5 6.5l3 1v1c0 1-1 2-2 2C4 10.5 1 7.5 1 3z"/></svg>13572468</li>
        <li><svg viewBox="0 0 12 12"><path d="M0 2h12v8H0z M0 2l6 4 6-4" /></svg>mark.dovan@velbrook-example.com</li>
        <li><svg viewBox="0 0 12 12"><circle cx="6" cy="6" r="6"/></svg>www.velbrook-example.com.my</li>
      </ul>
      <p class="tagline">Solving flow challenges,<br>exceeding expectations</p>
    </div>
  </section>

  <section class="card card-back" aria-label="Business card back">
    <div class="back-brand">
      <span class="brand-square"></span>
      <span class="brand-name">Velbrook Stream Systems</span>
    </div>
    <p class="product-lines">
      Pumping Technology<span class="sep">|</span>Valve &amp; Actuation<br>
      Air Moving Technology
    </p>
  </section>
</main>
</body>
</html>
```